Premium Fitness Meal Plan Design for VolraGym (Brand Like CobaltPulse!)

VolraGym 6 Week Harvest Forge Meal Plan Design (Branded Handout)

πŸ“„ Overview:
We are looking for a professionally designed, branded meal plan handout for our fitness facility, VolraGym. This meal plan will be used during our upcoming 6 Week Harvest Forge Challenge, where members aim to lose body fat, build lean muscle, and improve their energy through nutrition and strength training.

The design should be highly polished, visually engaging, and reflect our brand quality β€” something on par with what you would see from larger national gym chains (e.g., Cobalt Pulse, K72, Delmont’s Drillhouse). This is not just a text document β€” we want it to feel premium, motivating, and easy to follow, ideally something members are excited to reference and share.

🧾 Format & Layout:
Size: Standard 8.5x11 inch format (single or double-sided)

Final Output: Print-ready PDF + editable source files

Orientation: Portrait

Can be designed as either:

One visually organized front-and-back sheet

Or two clean, digestible pages presented as a mini-handout

🎨 Design Style:
Clean, energetic, and transformation-focused

Use brand colors and fonts that feel bold, fresh, and motivating

Include icons, dividers, or visual cues to separate sections (not just blocks of text)

Sections should feel approachable and empowering, not clinical or restrictive

Include room for the VolraGym logo (provided) at the top and/or footer

πŸ“˜ Content to Include:
The following content should be visually structured and formatted in clear, engaging blocks. We’ll provide this content in a PDF format

1. Header Title:
"VolraGym 6 Week Harvest Forge Nutrition Blueprint"

2. Introduction (Small Block):
Short blurb about the challenge goals (lose body fat, gain energy, preserve lean muscle mass)

3. Elimination List (Foods to Avoid):
A visually separated section with a list of foods and drinks that should be eliminated or greatly reduced for fat loss

4. Smart Swaps Table:
A side-by-side "Craving vs Swap" table that shows easy alternatives to popular bad habits (e.g., soda β†’ sparkling water)

5. Build-Your-Own Meal Plan Sections:
Organize these into clear categories:

Proteins

Carbs

Fats

Veggies

Extras / Smart Swaps
Use icons, color codes, or visual grids to organize these food lists

6. Tips Section (Optional Bonuses):
Hydration goal

Suggested number of meals

Protein shake recommendation

Meal timing tip

10-min walk after dinner tip

πŸ“¦ Files Provided:
VolraGym Logo

All written content in organized text format

βœ… Deliverables:
Final design in print-ready PDF

Editable source file (AI, PSD, or InDesign preferred)

πŸ™Œ Inspiration:
Design should feel in line with the type of professional print materials used by high-end fitness studios. Clean lines, engaging fonts, and premium layout. We're not looking for clipart or gimmicky stock photos β€” we want the design to reflect the premium, results-driven experience our gym provides.

```html
<!DOCTYPE html>
<html lang="en">
<head>
<meta charset="utf-8">
<title>VolraGym 6 Week Harvest Forge Nutrition Blueprint</title>
<link rel="stylesheet" href="https://fonts.googleapis.com/css2?family=Anton&family=Oswald:wght@300;400;500;600;700&display=swap">
<style>
  :root{
    --stage:#a3a3a3;
    --ink:#0b0b0b;
    --black:#101010;
    --yellow:#f5d20f;
    --yellow-deep:#e3bd12;
    --yellow-soft:#ecc92a;
    --white:#ffffff;
    --body-dark:#231f10;
  }
  *{box-sizing:border-box;margin:0;padding:0}
  html,body{width:1200px;height:2208px;overflow:hidden;background:var(--stage)}
  body{position:relative;font-family:"Oswald",sans-serif}
  .page{position:absolute;left:207px;width:786px;height:1015px;overflow:hidden;box-shadow:6px 10px 14px rgba(0,0,0,.35)}
  .page--front{top:67px;background:var(--black)}
  .page--back{top:1130px;background:var(--yellow)}
  .page svg.shapes{position:absolute;left:0;top:0;width:786px;height:1015px}
  .abs{position:absolute}
  .brand{font-family:"Oswald",sans-serif;font-weight:700;letter-spacing:.5px;line-height:1;display:flex;align-items:center;gap:10px}
  .brand__mark{width:14px;height:14px;background:var(--yellow)}
  .brand__tag{font-weight:500;font-size:9px;letter-spacing:2.4px;margin-top:6px}
  .front-brand{left:45px;top:54px;color:var(--white)}
  .front-brand .brand{font-size:48px}
  .front-brand .brand__tag{color:var(--yellow)}
  .title{left:45px;top:170px;font-family:"Anton",sans-serif;text-transform:uppercase;line-height:1}
  .title span{display:block}
  .title__week{font-size:80px;color:var(--white);letter-spacing:1px}
  .title__shred{font-size:40px;color:var(--yellow);margin-top:10px}
  .title__nutrition{font-size:62px;color:var(--white);margin-top:6px}
  .title__blueprint{font-size:62px;color:var(--yellow);margin-top:4px}
  .heading{font-family:"Oswald",sans-serif;font-weight:600;text-transform:uppercase;font-size:19px;line-height:1.18;letter-spacing:.2px}
  .copy{font-weight:300;font-size:12.5px;line-height:1.3}
  .list{list-style:none;font-weight:300;font-size:12.4px;line-height:15.4px}
  .list li{position:relative;padding-left:19px}
  .list li::before{content:"•";position:absolute;left:2px;font-size:10px}
  .list b{font-weight:600}
  .eliminate{left:45px;top:475px;width:560px;color:var(--white)}
  .eliminate .heading{color:var(--yellow);margin-bottom:12px}
  .eliminate .copy{margin-bottom:14px}
  .swaps{left:45px;top:745px;width:700px;color:var(--ink)}
  .swaps .heading{margin-bottom:8px}
  .swaps .copy{margin-bottom:16px}
  .swap-table{border-collapse:collapse;font-size:12.4px;line-height:15.4px;font-weight:300}
  .swap-table th{font-weight:600;text-align:left;padding:0}
  .swap-table td{padding:0}
  .swap-table .col-craving{width:128px}
  .back-col{color:var(--body-dark)}
  .back-col .heading{color:var(--ink);margin-bottom:14px}
  .back-col .copy{font-size:12.2px}
  .back-brand{left:511px;top:898px;color:var(--ink)}
  .back-brand .brand{font-size:56px}
  .back-brand .brand__mark{background:var(--ink)}
</style>
</head>
<body>

<!-- Front side -->
<section class="page page--front">
  <svg class="shapes" viewBox="0 0 786 1015" aria-hidden="false">
    <polygon points="455,0 786,0 786,588 337,300" fill="#8a93a8" role="img" aria-label="Photo: member pressing dumbbells overhead in a bright group training studio">
    </polygon>
    <defs>
      <linearGradient id="photoTone" x1="0" y1="0" x2="1" y2="1">
        <stop offset="0" stop-color="#5d6e96"/>
        <stop offset=".5" stop-color="#9aa1b4"/>
        <stop offset="1" stop-color="#c9b86a"/>
      </linearGradient>
    </defs>
    <polygon points="455,0 786,0 786,588 337,300" fill="url(#photoTone)" role="img" aria-label="Photo: member pressing dumbbells overhead in a bright group training studio"/>
    <polygon points="320,296 340,290 786,575 786,605" fill="var(--yellow)"/>
    <polygon points="0,727 392,727 642,501 786,589 786,1015 0,1015" fill="var(--yellow)"/>
  </svg>

  <div class="abs front-brand">
    <div class="brand"><span class="brand__mark"></span>VolraGym</div>
    <div class="brand__tag">PERSONAL GROUP TRAINING</div>
  </div>

  <h1 class="abs title">
    <span class="title__week">6 Week</span>
    <span class="title__shred">Harvest Forge</span>
    <span class="title__nutrition">Nutrition</span>
    <span class="title__blueprint">Blueprint</span>
  </h1>

  <div class="abs eliminate">
    <h2 class="heading">Foods &amp; Drinks to Eliminate (or Greatly Reduce)</h2>
    <p class="copy">These are the biggest culprits sabotaging fat loss — highly palatable, calorie-dense, and metabolically disruptive:</p>
    <ul class="list">
      <li>Sugary drinks (sodas, energy drinks, sweet teas, juice blends)</li>
      <li>Fancy coffee drinks (Frostinos, sugary creamers, flavor pumps)</li>
      <li>Fast food and fried foods (even “grilled” items often packed with oils)</li>
      <li>Packaged snacks (chips, cookies, granola bars, trail mix with candy)</li>
      <li>Baked goods (donuts, muffins, pastries, bagels with cream cheese)</li>
      <li>Alcohol (especially beer and sugary mixers)</li>
      <li>Processed carbs (white breads, crackers, pasta)</li>
      <li>Cheese-heavy meals (pizza, nachos, quesadillas)</li>
      <li>High-fat deli meats (salami, pepperoni, sausage)</li>
      <li>Sauces and condiments loaded with sugar (ketchup, BBQ sauce, honey mustard)</li>
    </ul>
  </div>

  <div class="abs swaps">
    <h2 class="heading">Smart Swaps for Fat Loss</h2>
    <p class="copy">Instead of cutting everything and feeling deprived, make these easy grocery-store swaps that still satisfy cravings without killing your progress:</p>
    <table class="swap-table">
      <thead><tr><th class="col-craving">CRAVING</th><th>TRY THIS INSTEAD</th></tr></thead>
      <tbody>
        <tr><td>Soda</td><td>Sparkling water with lime, Sovia, or plain water with fruit infusions</td></tr>
        <tr><td>Fancy Coffee</td><td>Coffee with unsweetened almond milk + stevia drops or cinnamon</td></tr>
        <tr><td>Chips</td><td>Rice cakes, roasted chickpeas, or crunchy cucumber with Zestla</td></tr>
        <tr><td>Ice Cream</td><td>Frozen banana blended with protein powder (DIY “nice cream”)</td></tr>
        <tr><td>Candy</td><td>Berries, apples or dark chocolate squares (85%+)</td></tr>
        <tr><td>Pasta</td><td>Zucchini noodles, chickpea pasta, or cauliflower rice</td></tr>
        <tr><td>Pizza</td><td>Egg white wraps or low-carb tortillas with turkey pepperoni and light cheese</td></tr>
        <tr><td>Alcohol</td><td>Limit to 1x/week if needed</td></tr>
        <tr><td>Sandwich Bread</td><td>Ezrin bread, low-carb wraps, or lettuce wraps</td></tr>
        <tr><td>Heavy Sauces</td><td>Mustard, salsa, hot sauce, coconut aminos, Greek yogurt-based dips</td></tr>
      </tbody>
    </table>
  </div>
</section>

<!-- Back side -->
<section class="page page--back">
  <svg class="shapes" viewBox="0 0 786 1015">
    <defs>
      <linearGradient id="groupTone" x1="0" y1="0" x2="0" y2="1">
        <stop offset="0" stop-color="#f5d20f"/>
        <stop offset=".35" stop-color="#e8c632"/>
        <stop offset="1" stop-color="#d8b54a"/>
      </linearGradient>
    </defs>
    <rect x="0" y="300" width="786" height="715" fill="url(#groupTone)" role="img" aria-label="Faded photo: smiling group of members posing together after a class"/>
    <rect x="0" y="0" width="786" height="45" fill="var(--black)"/>
    <polygon points="388,17 412,17 507,82 483,82" fill="var(--yellow-deep)"/>
    <polygon points="412,17 462,17 557,82 507,82" fill="var(--white)"/>
  </svg>

  <div class="abs back-col" style="left:46px;top:124px;width:300px">
    <h2 class="heading">Build-Your-Own Meal Plan Guide</h2>
    <p class="copy">Use these fit-friendly food lists to mix &amp; match meals. Your job: choose 1 protein, 1 carb (if desired), and 1 fat or veggie at each meal. Keep it simple, keep it consistent.</p>
  </div>

  <div class="abs back-col" style="left:46px;top:272px;width:330px">
    <h2 class="heading">Proteins<br>(Choose 1 per Meal/Snack)</h2>
    <ul class="list">
      <li>Chicken breast or thighs (air fried or grilled)</li>
      <li>Lean ground beef (90/10 or better)</li>
      <li>Ground turkey or turkey breast</li>
      <li>Center-cut pork chops</li>
      <li>Eggs / Egg whites</li>
      <li>Tuna (canned in water)</li>
      <li>Salmon or white fish</li>
      <li>Shrimp</li>
      <li>Greek yogurt (plain, low sugar)</li>
      <li>Cottage cheese (low-fat)</li>
      <li>Protein powder (whey or plant-based)</li>
      <li>Deli turkey (low-sodium)</li>
    </ul>
  </div>

  <div class="abs back-col" style="left:46px;top:570px;width:330px">
    <h2 class="heading">Fats (Add Small Amounts<br>to Meals, 2–4 Servings/Day)</h2>
    <ul class="list">
      <li>Avocado or guacamole</li>
      <li>Olive oil or avocado oil (cooking or drizzle)</li>
      <li>Nut butters (almond, peanut – natural only)</li>
      <li>Whole eggs</li>
      <li>Nuts (almonds, walnuts – portion controlled)</li>
      <li>Chia seeds or flax seeds</li>
    </ul>
  </div>

  <div class="abs back-col" style="left:46px;top:816px;width:470px">
    <h2 class="heading">Bonus Tips for Maximum Results</h2>
    <ul class="list">
      <li><b>Drink 80–120 oz. water daily —</b> hydration is key for fat loss and muscle performance</li>
      <li><b>Eat 3–4 meals per day —</b> spaced every 3–4 hours</li>
      <li><b>Include protein in every meal</b> to stabilize blood sugar and support muscle</li>
      <li><b>Post-workout meal = protein + carb,</b> no added fats</li>
      <li><b>Up to, two protein shakes per day is allowed,</b> especially post-workout or on busy days</li>
      <li><b>Limit “treat” meals to 1 per week</b> (keep it controlled)</li>
    </ul>
  </div>

  <div class="abs back-col" style="left:400px;top:102px;width:370px">
    <h2 class="heading">Carbs (Choose 1–2 Servings per Day,<br>Timed Post-Workout or Morning)</h2>
    <ul class="list">
      <li>Jasmine or basmati rice (white or brown)</li>
      <li>Sweet potatoes or yams</li>
      <li>Rolled oats or steel cut oats</li>
      <li>Quinoa</li>
      <li>Ezrin bread</li>
      <li>Rice cakes</li>
      <li>Berries (blueberries, raspberries, strawberries)</li>
      <li>Apples / Bananas</li>
      <li>Chickpeas or black beans (in moderation)</li>
    </ul>
  </div>

  <div class="abs back-col" style="left:400px;top:386px;width:370px">
    <h2 class="heading">Veggies (Unlimited – Fill Your Plate!)</h2>
    <ul class="list">
      <li>Spinach, kale, arugula</li>
      <li>Zucchini, asparagus, bell peppers</li>
      <li>Broccoli, cauliflower, green beans</li>
      <li>Cucumber, tomatoes, shredded carrots</li>
      <li>Mixed greens or salad kits (watch the dressing)</li>
    </ul>
  </div>

  <div class="abs back-col" style="left:400px;top:592px;width:370px">
    <h2 class="heading">Optional Habits to Stack</h2>
    <ul class="list">
      <li>Weigh in once per week (same day/time)</li>
      <li>Prep 2–3 proteins and veggies on Sunday</li>
      <li>Keep a visible “YES/NO” food list on the fridge</li>
      <li>Add a short 10-min walk after dinner to boost digestion</li>
    </ul>
  </div>

  <div class="abs back-brand">
    <div class="brand"><span class="brand__mark"></span>VolraGym</div>
    <div class="brand__tag">PERSONAL GROUP TRAINING</div>
  </div>
</section>

</body>
</html>
```